Vesprine Oakville Cabernet Sauvignon-Wine label design

We need a package design for an up market wine brand named, Vesprine. It will be a Cabernet Sauvignon from the Oakville AVA of Napa Valley. We are looking for a stylish modern label that will stand out on a retail shelf. We want the label to be attention grabbing and stylish while presenting an up market luxury brand.

Sick

Requirements
Must have
• Must have the words(in order of importance)
-Vesprine
-Cabernet Sauvignon
-Oakville
-Napa Valley
-2018

Must be designed for a traditional "Bordeaux" style bottle (Bottle specs in uploaded files)
Should not have
• Any images of grapes, vineyards, wine glasses or bottles

```html
<!DOCTYPE html>
<html lang="en">
<head>
<meta charset="utf-8">
<title>Vesprine Oakville Cabernet Sauvignon – Label</title>
<link href="https://fonts.googleapis.com/css2?family=Jost:wght@300;400;700&display=swap" rel="stylesheet">
<style>
  :root {
    --paper: #ffffff;
    --label-red: #ff3030;
    --ink: #1a1a1a;
    --reverse: #ffffff;
  }
  * { margin: 0; padding: 0; box-sizing: border-box; }
  html, body {
    width: 1200px;
    height: 4101px;
    overflow: hidden;
    background: var(--paper);
  }
  .canvas {
    position: relative;
    width: 1200px;
    height: 4101px;
    background: var(--paper);
  }
  .label {
    position: absolute;
    left: 0;
    top: 1636px;
    width: 1200px;
    height: 830px;
  }
  .band {
    position: absolute;
    background: var(--label-red);
    border-radius: 16px;
  }
  .band--full { border-radius: 0; }
  .brand-name {
    position: absolute;
    left: 0;
    width: 1200px;
    top: 206px;
    text-align: center;
    font-family: "Jost", sans-serif;
    font-weight: 700;
    font-size: 60px;
    line-height: 72px;
    letter-spacing: 0.32em;
    padding-left: 0.32em;
    color: var(--reverse);
    text-transform: uppercase;
  }
  .appellation {
    position: absolute;
    left: 274px;
    width: 834px;
    top: 322px;
    text-align: center;
    font-family: "Jost", sans-serif;
    font-weight: 300;
    font-size: 30px;
    line-height: 38px;
    letter-spacing: 0.3em;
    font-variant: small-caps;
    color: var(--reverse);
  }
  .varietal {
    position: absolute;
    left: 0;
    width: 1200px;
    top: 700px;
    text-align: center;
    font-family: "Jost", sans-serif;
    font-weight: 300;
    font-size: 40px;
    line-height: 50px;
    letter-spacing: 0.22em;
    font-variant: small-caps;
    color: var(--ink);
  }
  .vintage-row {
    position: absolute;
    left: 0;
    width: 1200px;
    top: 754px;
    height: 44px;
  }
  .vintage {
    position: absolute;
    left: 0;
    width: 1240px;
    text-align: center;
    font-family: "Jost", sans-serif;
    font-weight: 400;
    font-size: 30px;
    line-height: 44px;
    letter-spacing: 0.45em;
    color: var(--ink);
  }
  .rule {
    position: absolute;
    top: 22px;
    height: 2px;
    background: var(--ink);
  }
  .rule--left { left: 377px; width: 129px; }
  .rule--right { left: 729px; width: 138px; }
</style>
</head>
<body>
  <main class="canvas">
    <section class="label" aria-label="Vesprine Cabernet Sauvignon front label">
      <div class="band" style="left:140px; top:13px; width:933px; height:82px;"></div>
      <div class="band" style="left:236px; top:105px; width:639px; height:83px;"></div>
      <div class="band band--full" style="left:0; top:196px; width:1200px; height:99px;"></div>
      <div class="band" style="left:274px; top:301px; width:834px; height:81px;"></div>
      <div class="band" style="left:60px; top:392px; width:949px; height:82px;"></div>
      <div class="band" style="left:347px; top:484px; width:853px; height:89px;"></div>
      <div class="band" style="left:188px; top:583px; width:770px; height:83px;"></div>

      <h1 class="brand-name">Vesprine</h1>
      <p class="appellation">Oakville, Napa Valley</p>

      <p class="varietal">Cabernet Sauvignon</p>
      <div class="vintage-row">
        <span class="rule rule--left"></span>
        <span class="vintage">2018</span>
        <span class="rule rule--right"></span>
      </div>
    </section>
  </main>
</body>
</html>
```